Childcare Centre trifold brochure

Design a contemporary trifold brochure for a childcare centre that meets Australian printing requirements with supplied content, logo's, fonts and photo's. Please refer to the attached DL flyer front and back for similar possible style and content.

Target Market(s)

Families

Industry/Entity Type

Childcare

Requirements
Must have
• refer attached content, photo's, logo's and examples. Colours should be same as Pantone purple and green and or variations of. Refer attached dl flyer example.

```html
<!DOCTYPE html>
<html lang="en">
<head>
<meta charset="utf-8">
<title>Childcare Centre Trifold Brochure – Inside Spread</title>
<link href="https://fonts.googleapis.com/css2?family=Fira+Sans:ital,wght@0,300;0,400;1,300;1,400&display=swap" rel="stylesheet">
<style>
  :root {
    --page-light: #e6e7e9;
    --page-dark: #231f20;
    --purple-deep: #6d0b86;
    --purple-bright: #9c12b5;
    --green: #05a006;
    --white: #ffffff;
    --ink: #ffffff;
  }
  * { box-sizing: border-box; margin: 0; padding: 0; }
  html, body { width: 1200px; height: 934px; overflow: hidden; }
  body {
    position: relative;
    font-family: "Fira Sans", "Trebuchet MS", sans-serif;
    font-weight: 300;
    color: var(--ink);
    background: linear-gradient(to bottom, var(--page-light) 0 682px, var(--page-dark) 682px 100%);
  }
  .spread { position: absolute; left: 65px; top: 50px; width: 1071px; height: 834px; background: var(--white); }
  .photo { position: absolute; }
  .panel { position: absolute; }
  .panel-purple { background: linear-gradient(to right, var(--purple-deep), var(--purple-bright)); }

  /* columns */
  .photo-left-top { left: 65px; top: 50px; width: 358px; height: 192px;
    background: linear-gradient(160deg, #4e5b3a, #8a6f4c 55%, #b79a6a); }
  .panel-left { left: 65px; top: 250px; width: 363px; height: 436px; }
  .photo-left-bottom { left: 65px; top: 694px; width: 363px; height: 190px;
    background: linear-gradient(to bottom, #9cc2e0 0 12%, #b99c6e 30%, #6e4f33 100%); }

  .photo-mid-top { left: 431px; top: 50px; width: 345px; height: 192px;
    background: linear-gradient(135deg, #5b3d8a, #a4553e 45%, #d7a0c2 80%, #c9a04e); }
  .panel-mid { left: 430px; top: 242px; width: 350px; height: 642px; background: var(--green); }
  .panel-mid-foot { left: 430px; top: 805px; width: 350px; height: 79px; }
  .mid-slant { position: absolute; left: 430px; top: 802px; width: 350px; height: 24px; }

  .snap { border: 4px solid var(--white); }
  .snap-a { left: 435px; top: 235px; width: 180px; height: 192px; transform: rotate(-2deg);
    background: linear-gradient(160deg, #7a5fb0, #d8d3cc 45%, #8f7a5a); }
  .snap-b { left: 618px; top: 238px; width: 155px; height: 180px; transform: rotate(1.5deg);
    background: linear-gradient(160deg, #7a5fb0, #2f3550 45%, #8d7a60); }

  .photo-right-top { left: 785px; top: 50px; width: 351px; height: 192px;
    background: linear-gradient(to bottom, #dfe6e6 0 25%, #5f8a5a 45%, #c9c2b4 70%, #5a4634); }
  .panel-right { left: 782px; top: 250px; width: 354px; height: 436px; }
  .photo-right-bottom { left: 782px; top: 694px; width: 354px; height: 190px;
    background: linear-gradient(160deg, #b55a26, #8a4a2c 45%, #d9cfc4 85%); }

  /* copy */
  .copy { position: absolute; font-size: 12.8px; line-height: 16px; }
  .copy p + p { margin-top: 16px; }
  .copy-left { left: 104px; top: 289px; width: 300px; }
  .copy-mid { left: 463px; top: 465px; width: 300px; }
  .copy-right { left: 803px; top: 273px; width: 320px; }
  .source { font-size: 10px; line-height: 12px; font-weight: 400; }
  .source + .source { margin-top: 14px; }
  .copy-right .source + p { margin-top: 22px; }
  .pull-quote { font-style: italic; font-size: 14.4px; line-height: 17.5px; }
  .copy-mid .pull-quote { margin-top: 30px; }
  .copy-right .pull-quote { margin-top: 18px; font-size: 13.4px; line-height: 16.8px; }
</style>
</head>
<body>
  <div class="spread"></div>

  <div class="photo photo-left-top" role="img" aria-label="Natural playground with logs and sandstone boulders under native trees"></div>
  <section class="panel panel-purple panel-left"></section>
  <div class="photo photo-left-bottom" role="img" aria-label="Outdoor play yard with branch sculptures, sand pit and timber platform"></div>

  <div class="photo photo-mid-top" role="img" aria-label="Children in purple sun hats chopping vegetables on a timber deck"></div>
  <section class="panel panel-mid"></section>
  <div class="panel panel-purple panel-mid-foot"></div>
  <svg class="mid-slant" viewBox="0 0 350 24" aria-hidden="true">
    <polygon points="0,22 350,3 350,0 0,0" fill="var(--green)"/>
    <polygon points="0,22 350,3 350,6 0,25" fill="#111"/>
  </svg>
  <div class="photo snap snap-a" role="img" aria-label="Child in a sun hat and gloves using a hand tool on timber"></div>
  <div class="photo snap snap-b" role="img" aria-label="Child in a sun hat working with a hand drill outdoors"></div>

  <div class="photo photo-right-top" role="img" aria-label="Shaded outdoor play area with shade sails, cubby house and stepping stones"></div>
  <section class="panel panel-purple panel-right"></section>
  <div class="photo photo-right-bottom" role="img" aria-label="Carved timber water play feature set in white sand"></div>

  <div class="copy copy-left">
    <p>We are a Reggio Emilia inspired Childcare Centre offering long day care as well as a Nature Kindergarten program.</p>
    <p>At the core of our program is a Child-First ‘emergent curriculum’. An emergent Curriculum can be defined as a way of supporting learning that is based on the children’s interests.</p>
    <p>Learning occurs naturally and children thrive and learn best when their interests are considered and captured.</p>
    <p>Our children spend their days predominantly outdoors all year round, in one of two-amazing large Wildscape playgrounds full of native trees, a running creek bed, large stepping logs, herb, vegetable and bush tucker gardens, a worm farm, compost bin and chickens along with a recycled mud kitchen made by the children and a fire pit where the older children cook over an open fire.</p>
  </div>

  <div class="copy copy-mid">
    <p>In conjunction with our outdoor philosophy, throughout each school term our educators run free lessons for all ages in the following: yoga, meditation, sign language, Spanish, German, Malaysian, Sri Lankan Culture, sustainability, Noongar Culture &amp; Sport.</p>
    <p>The first five years of a child’s development are the most crucial with 90% of their brain synapsis being formed by this time.</p>
    <p class="pull-quote">“Early childhood is the most important time for brain development. It is the time in a child's life where they start building their brain connections and therefore, ultimately, the work we do will shape their life forever”.</p>
  </div>

  <div class="copy copy-right">
    <p class="source">Source:</p>
    <p class="source">The Growing Outdoors: Lessons for Tomorrow's Learners’ report, Published July 2017</p>
    <p>We believe that the best developmental outcomes occur when children who wander, wonder and play are also learning. It happens when children’s interests and passions are respected and nurtured and when educators shift their agenda away from imparting knowledge that we consider worthy, to showing children that we value their curiosity, problem solving, questions, and theories.</p>
    <p>Our Educators act as mentors for the children as they guide them through the adventure of learning outdoors in academic subjects such as science, technology, engineering and maths (STEM).</p>
    <p class="pull-quote">“Outdoor learning was added to the Australian Curriculum in 2015, however just 34% of teachers surveyed taught outdoors for 15 minutes or more” Source: The Growing Outdoors: Lessons for Tomorrow's Learners’ report, Published July 2017</p>
  </div>
</body>
</html>
```